Crime/mystery/thriller novel cover design

I am looking to get a cover designed for a novel. It is a crime/mystery/thriller set in Liverpool, England, between the 1970s and current day. I have permission to use some paintings by an artist for the cover, so it just needs put together and jazzed up. I am looking for something which has a fairly classic feel (so not just pulp airport thriller trash) but with some flair nonetheless.
The novel will be paperback, 127mm x 203mm with approx 18mm spine width. Can be gloss or matt cover, would be interesting to discuss.
The title is:
THE CASTLEMERE TIDE
Author name:
ROBERT J. KELVANSKI
Publisher:
VELUMBRA PUBLISHING LTD (or simply VELUMBRA)

I am still working on the back cover blurb but I will upload this when finished.
There are 4 images I could use for the cover though my favourite is the one called Evening, Harwick Docklands.

```html
<!DOCTYPE html>
<html lang="en">
<head>
<meta charset="utf-8">
<title>The Castlemere Tide — Robert J. Kelvanski</title>
<link rel="stylesheet" href="https://fonts.googleapis.com/css2?family=Almendra:wght@700&family=Josefin+Sans:wght@400;600&display=swap">
<style>
  :root {
    --backdrop: #e4e4e4;
    --ink-dark: #262725;
    --sky-grey: #3a3d36;
    --sky-green: #4c5641;
    --glow-yellow: #e8c13a;
    --glow-orange: #d9872e;
    --title-gold: #e2ab4f;
    --spine-white: #f1efe9;
  }
  * { margin: 0; padding: 0; box-sizing: border-box; }
  html, body { width: 1200px; height: 900px; overflow: hidden; }
  body {
    background: var(--backdrop);
    display: flex;
    align-items: center;
    justify-content: center;
  }
  .book {
    display: flex;
    height: 800px;
    box-shadow: 0 18px 40px rgba(0,0,0,0.18);
  }
  .spine {
    position: relative;
    width: 71px;
    height: 100%;
    background: linear-gradient(180deg, var(--ink-dark) 0%, var(--ink-dark) 68%, var(--sky-green) 76%, var(--glow-yellow) 86%, var(--glow-orange) 100%);
    overflow: hidden;
  }
  .spine-text {
    position: absolute;
    top: 24px;
    left: 50%;
    width: 740px;
    transform-origin: 0 0;
    transform: rotate(90deg) translateY(-50%);
    display: flex;
    align-items: center;
    gap: 30px;
    white-space: nowrap;
  }
  .spine-title {
    font-family: "Almendra", serif;
    font-weight: 700;
    font-size: 30px;
    color: var(--title-gold);
    letter-spacing: 1px;
  }
  .spine-title .the { font-size: 24px; margin-right: 22px; }
  .spine-author {
    margin-left: auto;
    margin-right: 36px;
    font-family: "Josefin Sans", sans-serif;
    font-size: 17px;
    letter-spacing: 3px;
    color: var(--spine-white);
  }
  .front {
    position: relative;
    width: 500px;
    height: 100%;
    overflow: hidden;
    border-left: 1px solid rgba(0,0,0,0.35);
  }
  .cover-painting {
    position: absolute;
    inset: 0;
    width: 100%;
    height: 100%;
  }
  .front-content {
    position: relative;
    text-align: center;
    padding-top: 118px;
  }
  .author {
    font-family: "Josefin Sans", sans-serif;
    font-weight: 600;
    font-size: 21px;
    letter-spacing: 4px;
    color: var(--title-gold);
  }
  .title {
    margin-top: 14px;
    font-family: "Almendra", serif;
    font-weight: 700;
    color: var(--title-gold);
    line-height: 0.95;
  }
  .title .the { display: block; font-size: 74px; }
  .title .main { display: block; font-size: 66px; letter-spacing: 2px; }
</style>
</head>
<body>
  <div class="book">
    <div class="spine">
      <div class="spine-text">
        <span class="spine-title"><span class="the">The</span>CASTLEMERE TIDE</span>
        <span class="spine-author">ROBERT J. KELVANSKI</span>
      </div>
    </div>
    <div class="front">
      <svg class="cover-painting" role="img" aria-label="Painting: Evening, Harwick Docklands — a dark waterfront skyline silhouetted against a glowing yellow and orange sky, reflected in the river" viewBox="0 0 500 800" preserveAspectRatio="none">
        <defs>
          <linearGradient id="sky" x1="0" y1="0" x2="0" y2="1">
            <stop offset="0" stop-color="#262725"/>
            <stop offset="0.3" stop-color="#2f312d"/>
            <stop offset="0.45" stop-color="#4c5641"/>
            <stop offset="0.58" stop-color="#3b4036"/>
            <stop offset="0.7" stop-color="#c9a53a"/>
            <stop offset="0.8" stop-color="#2c2b27"/>
            <stop offset="0.9" stop-color="#d9872e"/>
            <stop offset="1" stop-color="#e8b43e"/>
          </linearGradient>
          <radialGradient id="glow" cx="0.75" cy="0.68" r="0.5">
            <stop offset="0" stop-color="#e8c13a" stop-opacity="0.8"/>
            <stop offset="1" stop-color="#e8c13a" stop-opacity="0"/>
          </radialGradient>
        </defs>
        <rect width="500" height="800" fill="url(#sky)"/>
        <rect width="500" height="800" fill="url(#glow)"/>
      </svg>
      <div class="front-content">
        <p class="author">ROBERT J. KELVANSKI</p>
        <h1 class="title">
          <span class="the">The</span>
          <span class="main">CASTLEMERE</span>
          <span class="main">TIDE</span>
        </h1>
      </div>
    </div>
  </div>
</body>
</html>
```